I need a book cover designed for my e-book The Corner Shop Falconer.

The Corner Shop Falconer is a book about how to turn any small business into a success and is based on my experience building a cocktail bar. I am led in my journey by a stylish Japanese business expert in a sharp suit and a top knot.

The final design should stand out and grab people's attention while conveying the simplicity of the samurai.

I have attached a cover that I wish I could use (but obviously can't because of copyright).

I will need a JPEG file and at least 2500 pixels on the longest side with a height/weight ratio of 1.6

```html
<!DOCTYPE html>
<html lang="en">
<head>
<meta charset="utf-8">
<title>The Corner Shop Falconer — Book Cover</title>
<link rel="stylesheet" href="https://fonts.googleapis.com/css2?family=Great+Vibes&family=Cinzel:wght@400;600&family=Shojumaru&family=Montserrat:wght@800&display=swap">
<style>
  :root {
    --stage: #e8e5e1;
    --cover-core: #c61d1d;
    --cover-mid: #8d1114;
    --cover-edge: #1c0305;
    --title-red: #e0121a;
    --title-gold: #e6c21a;
    --gold-shade: #8a6a05;
    --ink: #120304;
    --figure-dark: #1d2a33;
    --figure-red: #a5161b;
  }
  * { margin: 0; padding: 0; box-sizing: border-box; }
  html, body {
    width: 1200px; height: 800px; overflow: hidden;
    background: var(--stage);
  }
  .stage {
    width: 1200px; height: 800px;
    display: flex; align-items: center; justify-content: center;
  }
  .book-cover {
    position: relative;
    width: 565px; height: 800px;
    overflow: hidden;
    background: radial-gradient(ellipse 75% 60% at 50% 55%, var(--cover-core) 0%, var(--cover-mid) 55%, var(--cover-edge) 100%);
    box-shadow: 0 10px 30px rgba(0,0,0,0.25);
  }
  .title { position: absolute; left: 0; right: 0; top: 0; height: 280px; }
  .title-script {
    position: absolute; left: 70px; top: 14px;
    font-family: "Great Vibes", cursive;
    font-size: 96px; line-height: 1;
    color: var(--title-red);
    transform: rotate(-4deg);
    white-space: nowrap;
  }
  .title-brush {
    position: absolute; left: 0; right: 0; top: 160px;
    text-align: center;
    font-family: "Shojumaru", cursive;
    font-size: 82px; line-height: 1;
    color: var(--title-red);
    letter-spacing: 0.02em;
    text-shadow: 0 3px 6px rgba(0,0,0,0.35);
  }
  .title-gold {
    position: absolute; left: 0; right: 0; top: 138px;
    text-align: center;
    font-family: "Cinzel", serif;
    font-weight: 600;
    font-size: 76px; line-height: 1;
    letter-spacing: 0.02em;
    color: var(--title-gold);
    text-shadow: 1px 2px 0 var(--gold-shade), 0 4px 8px rgba(0,0,0,0.4);
  }
  .tagline {
    position: absolute; left: 0; right: 0; top: 282px;
    text-align: center;
    font-family: "Montserrat", sans-serif;
    font-weight: 800;
    font-size: 12.5px; line-height: 18.5px;
    letter-spacing: 0.42em;
    color: var(--ink);
    text-transform: uppercase;
  }
  .cover-figure {
    position: absolute; left: 158px; top: 362px;
    width: 250px; height: 345px;
    border-radius: 46% 46% 30% 30%;
    background: radial-gradient(ellipse at 50% 40%, #34434d 0%, var(--figure-dark) 60%, rgba(29,42,51,0.85) 100%);
    box-shadow: 14px 8px 0 -4px var(--figure-red);
  }
  .author-name {
    position: absolute; left: 0; right: 0; top: 726px;
    text-align: center;
    font-family: "Cinzel", serif;
    font-size: 36px; line-height: 1;
    letter-spacing: 0.02em;
    color: var(--title-gold);
  }
</style>
</head>
<body>
  <main class="stage">
    <article class="book-cover">
      <header class="title">
        <div class="title-script">The Corner</div>
        <div class="title-brush">Falconer</div>
        <h1 class="title-gold">SHOP</h1>
      </header>
      <p class="tagline">Cutting through the crap to help<br>you and your business to be<br>the success you deserve</p>
      <div class="cover-figure" role="img" aria-label="Cartoon illustration of a crouching masked business warrior in a dark suit, red tie and red cape, holding a sword over his shoulder"></div>
      <p class="author-name">AUTHOR NAME</p>
    </article>
  </main>
</body>
</html>
```